Buchcover-Design für Fachbuch
Tolle Entwürfe und ein sehr effiziente Zusammenarbeit. Können wir nur weiterempfehlen.
Zielgruppe
Unternehmensberatung im Thema Arbeitszeit. Wir haben ein Fachbuch zum Thema Arbeitszeit und Personaleinsatzplanung für Geschäftsführer, HR Mitarbeiter, Führungskräfte, Studenten und alle geschrieben, die sich o.g. Themen näher informieren möchten
Aufgabenstellung
Folgende Textelemente sollen zu sehen sein:
Autorennamen: Dr. Reinhold Kattner, Lothar Brenning
Titel: PLAN STARK Betrieb - Dienstzeiten und Schichtorganisation fair, rentabel und marktnah einrichten
Außerdem: Unter Mitwirkung von Prof. Anton K. Ruhland
Und: mit vielen Praxisbeispielen (ggf. als eine Art Plakette)
Auf der Rückseite soll ein Klappentext und 2 Zitate zu sehen sein:
Klappentext:
Die Welt verändert sich dramatisch. Digitalisierung, Fachkräftemangel, Wertewandel und nicht zuletzt Ausnahmezustände wie die Coronakrise stellen Unternehmen vor große Herausforderungen. Wie können Unternehmen flexibel und gleichzeitig wirtschaftlich, kunden- und mitarbeiterorientiert agieren?
Reinhold Kattner und Lothar Brenning sehen eine innovative Arbeitszeitgestaltung als entscheidenden Hebel an, um Unternehmen aller Branchen in schnelllebigen Märkten flexibel aufzustellen. Die Autoren beleuchten mit vielen Beispielen aus ihrer Beratungspraxis, warum Arbeitszeitsysteme dringend modernisiert werden müssen und welche Möglichkeiten Sie bereits heute haben, Arbeitszeit innovativ zu gestalten.
Sie erfahren alles Wissenswerte über klassische Modelle, wie z.B. Schichtplan, Gleitzeit, Vertrauensarbeitszeit, Zeitkontensystem und Teilzeit, über Workforce Management (Workforce Analytics, Personalbedarfsermittlung und Forecast, Personaleinsatzplanung, Zeiterfassung) bis hin zu Lebensarbeitszeit, Gruppenarbeit, Selbstorganisation, Homeoffice und New Work. Dabei lernen Sie nicht nur die Einzelkomponenten kennen, sondern erfahren auch, wie man diese geschickt zu einer für Mitarbeiter und Unternehmen gleichermaßen vorteilhaften Arbeitszeitsystematik kombiniert. Neben diesem strategischen Wissen vermitteln Ihnen die Autoren hilfreiche Methoden zur konkreten operativen Umsetzung dieser Themen.
Zitat 1:
„Durch die Weitergabe ihrer umfassenden Erfahrungen aus der Beratung ist es den Autoren in hervorragender Weise gelu..

```html
<!DOCTYPE html>
<html lang="de">
<head>
<meta charset="utf-8">
<title>PLAN STARK Betrieb – Buchcover</title>
<link rel="stylesheet" href="https://fonts.googleapis.com/css2?family=Bebas+Neue&family=Roboto:wght@400&family=Fira+Sans:wght@300;400&display=swap">
<style>
  :root {
    --navy: #003a78;
    --green: #9bc53d;
    --band: #8f9dc3;
    --orange: #f0a800;
    --white: #ffffff;
    --paper: #ffffff;
  }
  * { margin: 0; padding: 0; box-sizing: border-box; }
  html, body { width: 848px; height: 1200px; overflow: hidden; background: var(--paper); }
  .canvas { position: relative; width: 848px; height: 1200px; }
  .cover { position: absolute; left: 81px; top: 190px; width: 686px; height: 889px; background: var(--white); outline: 1px solid #e4e4e4; }
  .block { position: absolute; }
  .photo { position: absolute; }
  .photo-doctors { left: 0; top: 0; width: 229px; height: 203px; background: linear-gradient(135deg, #f1f3f5, #d9dee4 60%, #c6ccd3); }
  .authors-panel { left: 229px; top: 0; width: 229px; height: 183px; background: var(--navy); display: flex; flex-direction: column; align-items: center; justify-content: center; padding-top: 6px; }
  .authors-band { left: 229px; top: 183px; width: 229px; height: 20px; background: var(--band); }
  .author { font-family: "Roboto", sans-serif; font-size: 22px; color: var(--white); line-height: 31px; }
  .photo-cashier { left: 458px; top: 0; width: 228px; height: 203px; background: linear-gradient(135deg, #7a6a58, #b8a892 50%, #8aa0c0); }
  .stripe-green { left: 0; top: 203px; width: 20px; height: 201px; background: var(--green); }
  .stripe-navy { left: 0; top: 404px; width: 20px; height: 80px; background: var(--navy); }
  .title { position: absolute; left: 42px; top: 230px; font-family: "Bebas Neue", sans-serif; }
  .title-main { font-size: 156px; line-height: 120px; letter-spacing: 1px; white-space: nowrap; }
  .title-main .plan { color: var(--green); }
  .title-main .stark { color: var(--navy); margin-left: 12px; }
  .title-sub { position: absolute; left: 340px; top: 380px; font-family: "Bebas Neue", sans-serif; font-size: 76px; line-height: 70px; color: var(--navy); letter-spacing: 3px; }
  .subtitle-band { left: 229px; top: 484px; width: 457px; height: 20px; background: var(--band); }
  .subtitle-panel { left: 229px; top: 504px; width: 457px; height: 183px; background: var(--navy); }
  .subtitle { position: absolute; left: 31px; top: 16px; font-family: "Fira Sans", sans-serif; font-weight: 300; font-size: 29px; line-height: 36px; color: var(--white); }
  .subtitle span { display: block; }
  .subtitle .l3 { padding-left: 25px; }
  .subtitle .l4 { padding-left: 56px; }
  .photo-office { left: 0; top: 487px; width: 229px; height: 202px; background: linear-gradient(135deg, #f3f3f2, #e6e2dc 55%, #cfc8bf); }
  .credit-panel { left: 0; top: 689px; width: 229px; height: 200px; background: var(--green); color: var(--white); text-align: center; font-family: "Roboto", sans-serif; }
  .credit-label { position: absolute; left: 0; right: 0; top: 83px; font-size: 15.5px; }
  .credit-name { position: absolute; left: 0; right: 0; top: 110px; font-size: 22px; }
  .photo-bakery { left: 229px; top: 687px; width: 457px; height: 202px; background: linear-gradient(135deg, #d8c9b0, #eee8de 50%, #b9b4ac); }
  .badge { position: absolute; left: 136px; top: 603px; width: 170px; height: 170px; }
  .badge-text { position: absolute; inset: 0; display: flex; flex-direction: column; align-items: center; justify-content: center; font-family: "Fira Sans", sans-serif; font-size: 26px; line-height: 28px; color: var(--white); transform: rotate(-6deg); }
</style>
</head>
<body>
<div class="canvas">
  <div class="cover">
    <div class="photo photo-doctors" role="img" aria-label="Foto: Ärzteteam bespricht sich am Laptop"></div>
    <div class="block authors-panel">
      <div class="author">Dr. Reinhold Kattner</div>
      <div class="author">Lothar Brenning</div>
    </div>
    <div class="block authors-band"></div>
    <div class="photo photo-cashier" role="img" aria-label="Foto: Verkäufer an der Supermarktkasse"></div>

    <div class="block stripe-green"></div>
    <div class="block stripe-navy"></div>
    <div class="title">
      <div class="title-main"><span class="plan">PLAN</span><span class="stark">STARK</span></div>
    </div>
    <div class="title-sub">BETRIEB</div>

    <div class="block subtitle-band"></div>
    <div class="block subtitle-panel">
      <div class="subtitle">
        <span>Dienstzeiten und Schicht-</span>
        <span>organisation fair, rentabel</span>
        <span class="l3">und marktnah</span>
        <span class="l4">einrichten</span>
      </div>
    </div>
    <div class="photo photo-office" role="img" aria-label="Foto: Mitarbeiterin am Laptop im Büro"></div>
    <div class="block credit-panel">
      <div class="credit-label">Unter Mitwirkung von</div>
      <div class="credit-name">Prof. Anton K. Ruhland</div>
    </div>
    <div class="photo photo-bakery" role="img" aria-label="Foto: Team in einer Großbäckerei bei der Arbeit"></div>

    <div class="badge">
      <svg width="170" height="170" viewBox="0 0 170 170" aria-hidden="true">
        <circle cx="85" cy="85" r="82" fill="var(--white)"/>
        <circle cx="85" cy="85" r="78" fill="var(--orange)"/>
      </svg>
      <div class="badge-text"><span>mit vielen</span><span>Praxis-</span><span>beispielen</span></div>
    </div>
  </div>
</div>
</body>
</html>
```